Business Cards, Stationery and Envelope Design
The Law Office of Gavin T. Morrell, P.A.
Professional
Gavin T. Morrell, Esq., LL.M.
Attorney at Law
2847 Heronwood Commerce Boulevard
Suite 214
Sunrise, FL 33319
gavin@gtmlegalgroup-example.com
www.gtmlegalgroup-example.com
Want logo to be on the business card, stationery and envelope. Would like to see writing in black but also a little color in the card, stationery and envelope other than just in the logo.
Business Formation & Structuring
Purchase & Sale of Business
Contract Review & Preparation
Shareholder Agreements
Loan Transactions
Tax Matters
Real Estate Closings
.ai file now uploaded
Attached is a file with my logo. Please let me know if you need it in another format.

```html
<!DOCTYPE html>
<html lang="en">
<head>
<meta charset="utf-8">
<title>Gavin T. Morrell, P.A. — Stationery Concepts</title>
<link href="https://fonts.googleapis.com/css2?family=Lato:wght@400;700&display=swap" rel="stylesheet">
<style>
:root{
  --bg:#e4d3b5;
  --paper:#ffffff;
  --ink:#1d1d1d;
  --muted:#6b6b6b;
  --green:#2f8a2c;
  --green-dark:#145a14;
  --green-light:#6fc35a;
  --charcoal:#3a3a3a;
  --faint:#e3e9e2;
  --label:#4a3b28;
}
*{margin:0;padding:0;box-sizing:border-box}
html,body{width:1200px;height:446px;overflow:hidden;background:var(--bg);font-family:"Lato",sans-serif;color:var(--ink)}
.canvas{position:relative;width:1200px;height:446px}
.sheet{position:absolute;background:var(--paper);box-shadow:0 2px 6px rgba(0,0,0,.25);overflow:hidden}
.label{position:absolute;font-size:7px;letter-spacing:.8px;text-transform:uppercase;color:var(--label);white-space:nowrap}
.brand{font-weight:700;color:var(--ink);white-space:nowrap}
.band{position:absolute;left:0;right:0;bottom:0}
.band-green{height:14px;background:linear-gradient(90deg,var(--green-light),var(--green) 55%,var(--green-dark))}
.band-dark{height:6px;background:var(--charcoal)}
.faint-name{position:absolute;font-weight:700;color:var(--faint);white-space:nowrap;text-align:center}
.small{font-size:4.5px;line-height:6px;color:var(--muted);white-space:nowrap}

/* business cards */
.card-front{left:22px;top:156px;width:124px;height:66px}
.card-front .brand{position:absolute;left:8px;top:8px;font-size:6px}
.card-front .details{position:absolute;left:8px;top:22px}
.card-front .name{font-size:5.5px;font-weight:700;color:var(--ink);line-height:7px}
.card-front .band-green,.card-back .band-green{height:5px;bottom:2px}
.card-front .band-dark,.card-back .band-dark{height:2px}
.card-back{left:22px;top:242px;width:124px;height:66px}
.card-back .brand{position:absolute;left:0;right:0;top:26px;text-align:center;font-size:6.5px}

/* letterheads */
.letterhead-1{left:168px;top:12px;width:216px;height:410px}
.letterhead-2{left:408px;top:12px;width:216px;height:410px}
.letterhead-1 .brand{position:absolute;left:14px;top:14px;font-size:7px}
.letterhead-1 .address{position:absolute;left:128px;top:12px;border-left:1px solid #ccc;padding-left:5px}
.letterhead-2 .brand{position:absolute;left:0;right:0;top:14px;text-align:center;font-size:7px}
.letterhead-1 .faint-name{left:0;right:0;top:300px;font-size:16px}
.letterhead-2 .faint-name{left:0;right:0;top:190px;font-size:16px}
.letterhead-2 .footer{position:absolute;left:0;right:0;bottom:24px;text-align:center}
.letterhead-1 .band-green,.letterhead-2 .band-green{bottom:6px}

/* envelopes */
.env{position:absolute;left:787px;width:413px;overflow:hidden}
.env svg{position:absolute;left:0;top:0}
.env-green{top:0;height:55px}
.env-dark{top:66px;height:68px}
.env-white{top:137px;height:92px;background:var(--paper);box-shadow:0 2px 6px rgba(0,0,0,.25)}
.env-white .brand{position:absolute;left:185px;top:40px;font-size:6.5px}
.env-front{left:787px;top:254px;width:413px;height:156px}
.env-front .brand{position:absolute;left:14px;top:16px;font-size:6.5px}
.env-front .return{position:absolute;left:14px;top:26px}
.env-front .faint-name{right:22px;top:70px;font-size:13px}
.env-front .band-green{height:10px;bottom:5px}
.env-front .band-dark{height:5px}
</style>
</head>
<body>
<main class="canvas">

  <p class="label" style="left:14px;top:130px">Stationery Concepts</p>

  <section class="sheet card-front" aria-label="Business card front">
    <p class="brand">Gavin T. Morrell, P.A.</p>
    <div class="details">
      <p class="name">Gavin T. Morrell, Esq., LL.M.</p>
      <p class="small">Attorney at Law<br>2847 Heronwood Commerce Boulevard, Suite 214<br>Sunrise, FL 33319<br>gavin@gtmlegalgroup-example.com</p>
    </div>
    <div class="band band-green"></div><div class="band band-dark"></div>
  </section>
  <p class="label" style="left:24px;top:229px">Business Card Front</p>

  <section class="sheet card-back" aria-label="Business card back">
    <p class="brand">Gavin T. Morrell, P.A.</p>
    <div class="band band-green"></div><div class="band band-dark"></div>
  </section>
  <p class="label" style="left:24px;top:315px">Business Card Back</p>

  <section class="sheet letterhead-1" aria-label="Letterhead option 1">
    <p class="brand">Gavin T. Morrell, P.A.</p>
    <p class="address small">2847 Heronwood Commerce Boulevard<br>Suite 214<br>Sunrise, FL 33319<br>www.gtmlegalgroup-example.com</p>
    <p class="faint-name">Gavin T. Morrell, P.A.</p>
    <div class="band band-green"></div><div class="band band-dark"></div>
  </section>
  <p class="label" style="left:240px;top:430px">Letterhead Option 1</p>

  <section class="sheet letterhead-2" aria-label="Letterhead option 2">
    <p class="brand">Gavin T. Morrell, P.A.</p>
    <p class="faint-name">Gavin T. Morrell, P.A.</p>
    <p class="footer small">2847 Heronwood Commerce Boulevard, Suite 214 · Sunrise, FL 33319<br>gavin@gtmlegalgroup-example.com · www.gtmlegalgroup-example.com</p>
    <div class="band band-green"></div><div class="band band-dark"></div>
  </section>
  <p class="label" style="left:478px;top:430px">Letterhead Option 2</p>

  <section class="env env-green" aria-label="Envelope back, green">
    <svg width="413" height="55" viewBox="0 0 413 55">
      <defs><linearGradient id="greenFill" x1="0" y1="0" x2="1" y2="1">
        <stop offset="0" stop-color="#5cb84a"/><stop offset="1" stop-color="#165c16"/></linearGradient></defs>
      <rect width="413" height="55" fill="url(#greenFill)"/>
    </svg>
  </section>

  <section class="env env-dark" aria-label="Envelope back, charcoal">
    <svg width="413" height="68" viewBox="0 0 413 68">
      <rect width="413" height="68" fill="#2e2e2e"/>
      <path d="M0 0 L206 40 L413 0 Z" fill="#3c3c3c"/>
      <path d="M0 68 L206 36 L413 68" fill="none" stroke="#1c1c1c" stroke-width="1.5"/>
    </svg>
  </section>

  <section class="env env-white" aria-label="Envelope back, white">
    <svg width="413" height="92" viewBox="0 0 413 92">
      <path d="M0 0 L206 70 L413 0" fill="none" stroke="#d6d6d6" stroke-width="1.5"/>
    </svg>
    <p class="brand">Gavin T. Morrell, P.A.</p>
  </section>

  <section class="sheet env-front" aria-label="Envelope option 2 front">
    <p class="brand">Gavin T. Morrell, P.A.</p>
    <p class="return small">2847 Heronwood Commerce Boulevard<br>Suite 214<br>Sunrise, FL 33319</p>
    <p class="faint-name">Gavin T. Morrell, P.A.</p>
    <div class="band band-green"></div><div class="band band-dark"></div>
  </section>
  <p class="label" style="left:930px;top:430px">Envelope Option 2</p>

</main>
</body>
</html>
```